Redesign Of Facebook Page Banner and Profile image

I just want to redesign my facebook page to be not so busy....more clean professional dental look. I dont like stock images so much so please go down the newsfeed to use an image or two from it...so it looks personable.

https://www.pagenook.com/RVMolarCareCo/

Target Market(s)

Consumers that care about their looks

Industry/Entity Type

Dental Clinic

Requirements
Must have
• I just want to redesign my facebook page to be not so busy....more clean professional modern look. I don't like stock images so much so please go down the newsfeed to use an image or two from it...so it looks personable.
• https://www.pagenook.com/RVMolarCareCo/
Nice to have
• I just want to redesign my facebook page to be not so busy....more clean professional dental look. I dont like stock images so much so please go down the newsfeed to use an image or two from it...so it looks personable.
Should not have

```html
<!DOCTYPE html>
<html lang="en">
<head>
<meta charset="utf-8">
<title>RV Molar Care Co — Page Cover and Profile Images</title>
<link href="https://fonts.googleapis.com/css2?family=Archivo:wght@600;700;800;900&family=Fira+Sans+Condensed:ital,wght@1,800&family=Roboto+Condensed:wght@700&display=swap" rel="stylesheet">
<style>
  :root {
    --board: #8fae83;
    --sky: #8fccf8;
    --sky-light: #bfe3fd;
    --sky-deep: #5ea9ea;
    --frame-line: #3d8fe0;
    --navy: #0b3d66;
    --white: #ffffff;
    --skin: #f1c9b0;
  }
  * { box-sizing: border-box; margin: 0; padding: 0; }
  html, body { width: 1200px; height: 1200px; overflow: hidden; }
  body { background: var(--board); font-family: "Archivo", sans-serif; position: relative; }

  .profile-set { position: absolute; left: 50px; top: 170px; display: flex; gap: 24px; }
  .profile {
    width: 240px; height: 240px; position: relative;
    display: flex; flex-direction: column; align-items: center; justify-content: center; gap: 14px;
    box-shadow: 0 2px 3px rgba(0,0,0,.25);
  }
  .profile--white { background: linear-gradient(180deg, var(--sky-light) 0%, var(--white) 70%); }
  .profile--blue { background: var(--sky); }
  .profile__mark { width: 120px; height: 120px; border-radius: 50%; background: var(--white); border: 4px solid var(--frame-line); }
  .profile__name { font-weight: 700; font-size: 20px; color: var(--navy); letter-spacing: .5px; }

  .cover {
    position: absolute; left: 50px; top: 500px; width: 1100px; height: 419px;
    background: var(--sky); overflow: hidden;
  }
  .cover__shapes { position: absolute; inset: 0; }
  .cover__photo {
    position: absolute; right: 0; top: 0; width: 420px; height: 100%;
    background: linear-gradient(90deg, rgba(143,204,248,0) 0%, rgba(241,201,176,.55) 35%, var(--skin) 70%, #c98f74 100%);
  }
  .cover__frame { position: absolute; left: 16px; top: 16px; right: 16px; bottom: 16px; border: 1.5px solid var(--frame-line); }
  .cover__copy { position: absolute; left: 55px; top: 78px; }
  .cover__eyebrow { font-weight: 800; font-size: 29px; letter-spacing: 2.5px; color: var(--white); }
  .cover__headline { font-weight: 900; font-size: 66px; line-height: 1; color: var(--navy); letter-spacing: 1px; margin-top: 6px; }
  .cover__script { font-family: "Fira Sans Condensed", sans-serif; font-style: italic; font-weight: 800; font-size: 44px; letter-spacing: 3px; color: var(--white); margin-top: 10px; }
  .cover__cta {
    display: inline-block; margin-top: 14px; background: var(--navy); color: var(--white);
    font-weight: 700; font-size: 18px; letter-spacing: -.2px; padding: 16px 19px 16px 20px;
  }
  .cover__phone { font-family: "Roboto Condensed", sans-serif; font-weight: 700; font-size: 40px; color: var(--white); margin-top: 8px; letter-spacing: .5px; }
  .cover__web { font-weight: 700; font-size: 17px; color: var(--white); letter-spacing: -.3px; margin-top: 6px; }
</style>
</head>
<body>
  <section class="profile-set">
    <div class="profile profile--white">
      <div class="profile__mark"></div>
      <div class="profile__name">RV Molar Care Co</div>
    </div>
    <div class="profile profile--blue">
      <div class="profile__mark"></div>
      <div class="profile__name">RV Molar Care Co</div>
    </div>
  </section>

  <section class="cover">
    <svg class="cover__shapes" width="1100" height="419" viewBox="0 0 1100 419">
      <polygon points="0,0 96,0 0,96" fill="#b6dcfb"/>
      <polygon points="628,70 670,55 690,107" fill="#5ea9ea" opacity=".8"/>
      <polygon points="572,196 592,182 598,222" fill="#5ea9ea" opacity=".8"/>
      <polygon points="436,380 512,340 514,398" fill="#5ea9ea" opacity=".75"/>
    </svg>
    <div class="cover__photo" role="img" aria-label="Photo of a smiling client with bright white teeth, hand raised beside her cheek"></div>
    <div class="cover__frame"></div>
    <div class="cover__copy">
      <div class="cover__eyebrow">PROFESSIONAL</div>
      <div class="cover__headline">LASER TEETH</div>
      <div class="cover__script">Whitening</div>
      <div class="cover__cta">SCHEDULE AN APPT TODAY</div>
      <div class="cover__phone">555.014.2876</div>
      <div class="cover__web">WWW.RVMOLARCARECO.COM</div>
    </div>
  </section>
</body>
</html>
```